Premium men's gut health supplement needs a bottle label designed

We’re velnora - a premium men’s wellness brand focused on gut health. Our first product is a high-quality daily supplement designed to support digestion, regularity, and internal cleanliness. Backed by science and tailored for modern lifestyles, velnora is crafted in the UK and proudly LGBT-owned. It aims to resolve intimacy problems that gay men may experience due to poor digestion but also does not exclude any other orientation - other men may use it simply to improve their digestion.

velnora is for health-conscious men who value science-backed supplements and want to feel confident from the inside out. Many of our early adopters will be gay and bisexual men who prioritise gut health as part of their self-care, sexual, and hygiene routine, though the product is equally effective and appealing to anyone seeking premium digestive support.

The product is premium the target customer is male, not specific to one location but primary markets will be US, UK and EU.

I’d like a supplement bottle designed for velnora, our premium men’s gut health brand. The focus should be clean, slightly clinical, and minimal - inspired by brands like Quelrin and Darvo. The key element is the wordmark (velnora) on the front, with no additional logo or icon. Lowercase text and a strong, contemporary font are preferred.

The bottle should be aesthetically pleasing so that people are proud to display it on their shelf, instead of hiding it in a cupboard (like Quelrin, darvo, Pia Venturek, Morvanel etc)

Avoid anything that shows the product as being for LGBT, e.g., no rainbows, men holding hands etc.

The design should be premium, minimalist and not be busy or overwhelming.

I have uploaded a file called "Bottle" to give an idea of the type of container, but please ignore the colours and change as you see fit. This is just for reference for the type of bottle we'll use - all colours are customisable.

I have also uploaded some images for "style" reference, e.g., darvo, quelrin, pia venturek, etc for inspiration.

```html
<!DOCTYPE html>
<html lang="en">
<head>
<meta charset="utf-8">
<title>velnora — Men's Gut Health Supplement Label</title>
<link href="https://fonts.googleapis.com/css2?family=Montserrat:wght@400;600&display=swap" rel="stylesheet">
<style>
  :root {
    --backdrop: #ebe8e3;
    --label-white: #ffffff;
    --brand-teal: #57bfbf;
    --ink: #222222;
    --on-teal: #ffffff;
  }
  html, body {
    margin: 0;
    padding: 0;
    width: 1200px;
    height: 964px;
    overflow: hidden;
    background: var(--backdrop);
  }
  .canvas {
    position: relative;
    width: 1200px;
    height: 964px;
  }
  .label {
    position: absolute;
    left: 273px;
    top: 52px;
    width: 653px;
    height: 860px;
    background: var(--label-white);
    box-shadow: 0 4px 14px rgba(0, 0, 0, 0.12);
    font-family: "Montserrat", Arial, sans-serif;
  }
  .label__band {
    position: absolute;
    left: 0;
    top: 56px;
    width: 100%;
    height: 197px;
    background: var(--brand-teal);
    color: var(--on-teal);
    text-align: center;
  }
  .label__band-line {
    position: absolute;
    left: 0;
    width: 100%;
    margin: 0;
    font-size: 21px;
    font-weight: 400;
    letter-spacing: 0.5px;
    line-height: 1;
  }
  .label__band-line--top { top: 47px; }
  .label__band-line--main { top: 89px; font-weight: 600; }
  .label__band-line--bottom { top: 132px; }
  .wordmark {
    position: absolute;
    left: 82px;
    top: 606px;
    margin: 0;
    font-family: "Montserrat", Arial, sans-serif;
    font-weight: 400;
    font-size: 84px;
    line-height: 1;
    letter-spacing: 2px;
    color: var(--ink);
  }
  .label__footer {
    position: absolute;
    top: 753px;
    left: 0;
    width: 100%;
    font-size: 17px;
    line-height: 1;
  }
  .label__spec {
    position: absolute;
    top: 0;
    margin: 0;
    color: var(--ink);
    white-space: nowrap;
  }
  .label__spec--count { left: 89px; }
  .label__spec--type { left: 266px; color: var(--brand-teal); }
  .label__spec--weight { left: 522px; }
</style>
</head>
<body>
  <main class="canvas">
    <section class="label" aria-label="velnora supplement bottle label">
      <div class="label__band">
        <p class="label__band-line label__band-line--top">PREMIUM</p>
        <p class="label__band-line label__band-line--main">MEN'S GUT HEALTH</p>
        <p class="label__band-line label__band-line--bottom">SUPPLEMENT</p>
      </div>
      <h1 class="wordmark">velnora</h1>
      <div class="label__footer">
        <p class="label__spec label__spec--count">60 CAPSULES</p>
        <p class="label__spec label__spec--type">DIETARY SUPPLEMENT</p>
        <p class="label__spec label__spec--weight">190g</p>
      </div>
    </section>
  </main>
</body>
</html>
```